Vantrel Ashcombe LLC

we need a business card design

Industry/Entity Type

hvac

Contact Information for Business Card

my logo

Requirements
Must have
• my logo and same colors

```html
<!DOCTYPE html>
<html lang="en">
<head>
<meta charset="UTF-8">
<title>Vantrel Ashcombe LLC – Business Card</title>
<link href="https://fonts.googleapis.com/css2?family=Montserrat:wght@400;500;700&display=swap" rel="stylesheet">
<style>
  :root {
    --backdrop: #2b2b2d;
    --card-blue: #0f5fa9;
    --accent-sky: #2aa9e2;
    --accent-gold: #f2b248;
    --text-white: #ffffff;
  }
  * { box-sizing: border-box; margin: 0; padding: 0; }
  html, body {
    width: 1200px; height: 875px; overflow: hidden;
    background: var(--backdrop);
    font-family: "Montserrat", sans-serif;
  }
  .stage {
    position: relative; width: 1200px; height: 875px;
    display: flex; align-items: center; justify-content: center; gap: 50px;
  }
  .card {
    position: relative; width: 520px; height: 297px;
    background: var(--card-blue); border-radius: 22px;
    color: var(--text-white);
  }
  .card-front {
    display: flex; align-items: center; justify-content: center; gap: 14px;
  }
  .brand-mark {
    width: 22px; height: 22px; border-radius: 50%;
    background: var(--accent-gold); flex: none;
  }
  .brand-name {
    font-weight: 700; font-size: 30px; line-height: 1.1;
    color: var(--text-white); text-transform: uppercase; letter-spacing: 0.5px;
  }
  .card-front .brand-name { text-align: left; }
  .card-back .brand-block {
    position: absolute; right: 32px; top: 56px;
    display: flex; align-items: center; gap: 10px;
  }
  .card-back .brand-name { font-size: 20px; }
  .card-back .brand-mark { width: 16px; height: 16px; }
  .details {
    position: absolute; left: 36px; bottom: 36px; width: 250px;
  }
  .person-name {
    font-weight: 700; font-size: 24px; color: var(--accent-sky);
    text-transform: uppercase; letter-spacing: 0.5px; line-height: 1;
  }
  .person-role { font-size: 13px; margin-top: 4px; }
  .rule { height: 1px; background: var(--accent-gold); margin: 10px 0; }
  .address { font-size: 12.5px; line-height: 1.35; }
  .contact-list { list-style: none; font-size: 12.5px; line-height: 1.6; }
  .contact-list li { display: flex; align-items: center; gap: 8px; }
  .contact-list svg { width: 12px; height: 12px; flex: none; fill: var(--accent-gold); }
</style>
</head>
<body>
<main class="stage">
  <section class="card card-front">
    <span class="brand-mark"></span>
    <span class="brand-name">Vantrel<br>Ashcombe LLC</span>
  </section>

  <section class="card card-back">
    <div class="brand-block">
      <span class="brand-mark"></span>
      <span class="brand-name">Vantrel<br>Ashcombe LLC</span>
    </div>
    <div class="details">
      <p class="person-name">Dorian Velk</p>
      <p class="person-role">Founder</p>
      <div class="rule"></div>
      <p class="address">24 Harlow Crest Rd<br>Marbury XYZ 4102</p>
      <div class="rule"></div>
      <ul class="contact-list">
        <li>
          <svg viewBox="0 0 24 24"><path d="M6.6 10.8a15.1 15.1 0 0 0 6.6 6.6l2.2-2.2a1 1 0 0 1 1-.25 11.4 11.4 0 0 0 3.6.57 1 1 0 0 1 1 1V20a1 1 0 0 1-1 1A17 17 0 0 1 3 4a1 1 0 0 1 1-1h3.5a1 1 0 0 1 1 1c0 1.25.2 2.45.57 3.57a1 1 0 0 1-.25 1z"/></svg>
          555.210.4836
        </li>
        <li>
          <svg viewBox="0 0 24 24"><path d="M2 5h20v14H2z M2 5l10 8 10-8" /></svg>
          info@vantrelashcombe.com
        </li>
        <li>
          <svg viewBox="0 0 24 24"><circle cx="12" cy="12" r="10"/></svg>
          www.vantrelashcombe.com
        </li>
      </ul>
    </div>
  </section>
</main>
</body>
</html>
```